Company document Header needed

Using our current logo, I need a Designer to create a header for use on our company documents. This header will include our business address, phone, fax, website address

Reason: Dear designers, I am so pleased with the many different options that have been presented, that I wish to purchase several of them from a few different designers. I will get with the pixel forum folks and figure out what is the best way to do this. In the meantime, I am extending the deadline to allow for a few edits such as our phone number and such. thanks to you all for your excellent work. RT

Designers,

Please take a look and edit any of your submissions that have incorrect info on them:  the correct info is below:

Business name is: Brass Kite, Inc.

website address is:  www.brasskite-example.com

Office #:  (855) BrassKite  

Fax#:  (858) 516-2947  (generally I do not intend to need this on any materials unless it balances a look)

email:  info@brasskite-example.com

Address:  782 Larkwood Blvd. suite 2310  San Diego, CA  92174

Thanks!

```html
<!DOCTYPE html>
<html lang="en">
<head>
<meta charset="utf-8">
<title>Brass Kite, Inc. Letterhead</title>
<link rel="stylesheet" href="https://fonts.googleapis.com/css2?family=Mali:wght@600&display=swap">
<style>
  :root {
    --paper: #ffffff;
    --ink: #000000;
    --band: #000000;
    --band-text: #ffffff;
  }
  html, body {
    margin: 0;
    padding: 0;
    overflow: hidden;
    background: var(--paper);
  }
  .page {
    position: relative;
    width: 931px;
    height: 1200px;
    background: var(--paper);
    overflow: hidden;
    font-family: "Mali", "Comic Sans MS", sans-serif;
    font-weight: 600;
  }
  .header-frame {
    position: absolute;
    left: 3px;
    top: 3px;
    width: 918px;
    height: 112px;
    border: 2px solid var(--ink);
    box-shadow: 3px 3px 0 var(--ink);
  }
  .header-band {
    position: absolute;
    left: 117px;
    top: 18px;
    width: 701px;
    height: 89px;
    background: var(--band);
    color: var(--band-text);
  }
  .brand-square {
    position: absolute;
    left: 30px;
    top: 7px;
    width: 36px;
    height: 36px;
    border: 3px solid var(--band-text);
    box-sizing: border-box;
  }
  .brand-name {
    position: absolute;
    left: 8px;
    top: 57px;
    font-size: 16px;
    line-height: 20px;
    letter-spacing: 0.3px;
  }
  .contact {
    position: absolute;
    font-size: 14px;
    line-height: 23px;
    letter-spacing: -0.2px;
    white-space: nowrap;
  }
  .contact-web { left: 112px; top: 56px; }
  .contact-phone { left: 284px; top: 33px; }
  .contact-address { left: 478px; top: 33px; }
  .contact p { margin: 0; }
</style>
</head>
<body>
<div class="page">
  <div class="header-frame"></div>
  <header class="header-band">
    <div class="brand-square"></div>
    <div class="brand-name">BRASSKITE</div>
    <div class="contact contact-web"><p>brasskite-example.com</p></div>
    <div class="contact contact-phone">
      <p>phone: 855.BrassKite</p>
      <p>fax: 858.516.2947</p>
    </div>
    <div class="contact contact-address">
      <p>782 Larkwood Blvd, suite 2310</p>
      <p>San Diego, CA 92174</p>
    </div>
  </header>
</div>
</body>
</html>
```